Need a website created on loftmarrow.com only

I need my website updated and created on loftmarrow.com only. I will provide you with marketing materials to design the website.

www.quernsmithy.io

Examples of sites that I would like my site to look like,

https://velbordtiles.com

You can use https://velbordtiles.com for content since we sell the same services

You can create a free account on loftmarrow.com to design the website.
Updates

reminder that this project must be built on loftmarrow.com or uploaded to loftmarrow.com you can create a free account. Added Saturday, January 7, 2017

Industry/Entity Type

Marketing

Number of Pages Required

1 page

Requirements
Must have
• must be uploaded or created on loftmarrow.com before the job is approved.

```html
<!DOCTYPE html>
<html lang="en">
<head>
<meta charset="utf-8">
<title>App Functionality List 2017</title>
<link rel="stylesheet" href="https://fonts.googleapis.com/css2?family=Exo+2:wght@200;300;400;600;800&display=swap">
<style>
  :root {
    --night: #07090d;
    --sky: #31b3e5;
    --login: #3bb6e3;
    --teal: #0e5a7a;
    --white: #ffffff;
    --ink: #555d66;
    --rule-light: rgba(255,255,255,0.45);
    --rule-grey: #c9ced3;
  }
  * { box-sizing: border-box; margin: 0; padding: 0; }
  html, body { width: 1152px; height: 1200px; overflow: hidden; }
  body {
    position: relative;
    font-family: "Exo 2", Arial, sans-serif;
    background: var(--white);
  }
  .backdrop { position: absolute; inset: 0; }

  .site-header {
    position: absolute; left: 0; top: 0; width: 1152px; height: 78px;
    border-bottom: 1px solid rgba(255,255,255,0.22);
  }
  .brand {
    position: absolute; left: 120px; top: 24px; display: flex; align-items: center; gap: 12px;
    color: var(--white);
  }
  .brand-mark { width: 24px; height: 24px; border: 3px solid var(--white); border-radius: 3px; }
  .brand-name { font-size: 26px; font-weight: 600; line-height: 1; }
  .main-nav a {
    position: absolute; top: 38px; color: var(--white); text-decoration: none;
    font-size: 16px; font-weight: 400;
  }
  .login-btn {
    position: absolute; left: 899px; top: 30px; width: 133px; height: 35px;
    background: var(--login); color: var(--white); border-radius: 3px;
    font-size: 16px; display: flex; align-items: center; justify-content: center;
  }

  .hero-title { position: absolute; left: 118px; top: 254px; color: var(--white); }
  .hero-title .lead { display: block; font-size: 37px; font-weight: 300; line-height: 1.1; }
  .hero-title .big { display: block; font-size: 56px; font-weight: 800; line-height: 1.1; }
  .btn-solid {
    position: absolute; left: 119px; top: 382px; width: 131px; height: 37px;
    background: var(--teal); color: var(--white); border-radius: 2px;
    font-size: 16px; display: flex; align-items: center; justify-content: center;
  }
  .slider-dots { position: absolute; left: 985px; top: 457px; display: flex; gap: 4px; }
  .slider-dots span { width: 12px; height: 12px; border-radius: 50%; background: var(--sky); }
  .slider-dots span.active { background: var(--white); }

  .device { position: absolute; border-radius: 26px; }
  .device-hero {
    left: 660px; top: 110px; width: 170px; height: 380px;
    background: linear-gradient(160deg, #2a2f35, #050608 60%);
    transform: rotate(-27deg); border: 3px solid #6c737a;
  }
  .device-map {
    left: 165px; top: 587px; width: 165px; height: 430px;
    background: linear-gradient(180deg, #2e3b47 0%, #d9cf9c 35%, #bfd4a6 70%, #2e3b47 100%);
    border: 4px solid #2a2e33;
  }
  .device-find {
    left: 815px; top: 915px; width: 185px; height: 300px;
    background: linear-gradient(180deg, #2a2e33 0%, #8fcf6a 18%, #e6e4dc 40%, #cfd8cf 100%);
    border: 4px solid #2a2e33;
  }

  .section-title { position: absolute; font-weight: 200; line-height: 1; }
  .about-title { left: 432px; top: 598px; font-size: 62px; color: var(--white); }
  .about-rule { position: absolute; left: 432px; top: 664px; width: 600px; height: 1px; background: var(--rule-light); }
  .about-copy {
    position: absolute; left: 432px; top: 692px; width: 600px;
    color: var(--white); font-size: 12px; line-height: 21.6px;
  }
  .btn-outline {
    position: absolute; left: 432px; top: 826px; width: 132px; height: 38px;
    border: 1px solid var(--white); border-radius: 2px; color: var(--white);
    font-size: 13px; font-weight: 600; display: flex; align-items: center; justify-content: center;
  }
  .contact-title { left: 118px; top: 1072px; font-size: 60px; color: var(--sky); }
  .contact-rule { position: absolute; left: 120px; top: 1139px; width: 600px; height: 1px; background: var(--rule-grey); }
  .contact-copy {
    position: absolute; left: 120px; top: 1168px; width: 600px;
    color: var(--ink); font-size: 12px; line-height: 21.6px;
  }
</style>
</head>
<body>
  <svg class="backdrop" width="1152" height="1200" viewBox="0 0 1152 1200" aria-hidden="true">
    <defs>
      <radialGradient id="heroGlow" cx="0.5" cy="0.45" r="0.6">
        <stop offset="0" stop-color="#2e343b"/>
        <stop offset="1" stop-color="#07090d"/>
      </radialGradient>
      <linearGradient id="pale" x1="0" y1="0" x2="1" y2="1">
        <stop offset="0" stop-color="#ffffff"/>
        <stop offset="1" stop-color="#d6ecf6"/>
      </linearGradient>
      <linearGradient id="blueTint" x1="0" y1="0" x2="1" y2="1">
        <stop offset="0" stop-color="#1f8fd0"/>
        <stop offset="1" stop-color="#31b3e5"/>
      </linearGradient>
    </defs>
    <rect width="1152" height="600" fill="url(#heroGlow)"/>
    <polygon points="0,584 1152,472 1152,1200 0,1200" fill="var(--sky)"/>
    <polygon points="0,584 330,552 330,1010 0,1048" fill="url(#blueTint)" opacity="0.7"/>
    <polygon points="0,1048 1152,840 1152,1200 0,1200" fill="url(#pale)"/>
  </svg>

  <header class="site-header">
    <div class="brand">
      <span class="brand-mark"></span>
      <span class="brand-name">Brightpane Apps</span>
    </div>
    <nav class="main-nav">
      <a href="#" style="left:410px">Industries</a>
      <a href="#" style="left:529px">Reseller</a>
      <a href="#" style="left:636px">Support</a>
      <a href="#" style="left:742px">Blog</a>
      <a href="#" style="left:822px">Contact</a>
    </nav>
    <a class="login-btn">Log In</a>
  </header>

  <section class="hero">
    <h1 class="hero-title"><span class="lead">App Functionality</span><span class="big">List 2017</span></h1>
    <a class="btn-solid">Read More</a>
    <div class="device device-hero" role="img" aria-label="Black smartphone with a dark screen"></div>
    <div class="slider-dots"><span></span><span class="active"></span><span></span></div>
  </section>

  <section class="about">
    <div class="device device-map" role="img" aria-label="Smartphone showing a laundry delivery app with a city map and pins"></div>
    <h2 class="section-title about-title">Around Us</h2>
    <div class="about-rule"></div>
    <p class="about-copy">Lorem ipsum dolor sit amet, consectetur adipiscing elit. In magna metus, vulputate in ultricies vitae, dignissim at purus. Mauris aliquet lorem quis ex fringilla, vitae bibendum eros blandit. Suspendisse id accumsan libero. Curabitur ex sapien, scelerisque sit amet nisi ut, ultricies egestas velit. Vestibulum ante ipsum primis in faucibus orci luctus et ultrices posuere cubilia Curae; Ut sodales maximus quam quis mollis. Maecenas id lacinia elit.Lorem ipsum dolor sit amet, consectetur adipiscing elit.</p>
    <a class="btn-outline">Read More</a>
  </section>

  <section class="contact">
    <div class="device device-find" role="img" aria-label="Smartphone showing a find-us screen with a street map"></div>
    <h2 class="section-title contact-title">Contact</h2>
    <div class="contact-rule"></div>
    <p class="contact-copy">Lorem ipsum dolor sit amet, consectetur adipiscing elit. In magna metus, vulputate in ultricies vitae, dignissim at purus. Mauris aliquet lorem quis ex fringilla, vitae bibendum eros blandit. Suspendisse id accumsan libero.</p>
  </section>
</body>
</html>
```